Verostel business card

Business card for sustainable investment company called "Verostel". Verostel is an exchange platform selling carbon credits between buyers and sellers. Carbon Credits are an environmental commodity for reducing global carbon emissions.

the card should obviously have our logo and the theme should be sustainability/environment mixed with a trading platform.

Contact Information for Business Card

Logo, Name, Title, Phone, Email

Colors
0054AA
0677BA
7BADD7
CADEEF
E8F1F8
0094D4
00A9DD
6FCCEA
C7EBF8
E9F6FB
00AB8E
00BBA5
67D7C9
C6EFE9
E9F9F6
59FF00
82FF00
B8FF75
E3FFCB
F4FFEA

```html
<!DOCTYPE html>
<html lang="en">
<head>
<meta charset="utf-8">
<title>Verostel business card</title>
<link rel="stylesheet" href="https://fonts.googleapis.com/css2?family=Poppins:wght@400;600&display=swap">
<style>
  :root {
    --backdrop: #9a9a9a;
    --card-navy: #22344e;
    --aqua: #35e6ee;
    --sky: #29a6ec;
    --azure: #2f7de8;
    --white: #ffffff;
  }
  * { margin: 0; padding: 0; box-sizing: border-box; }
  html, body {
    width: 1093px;
    height: 1200px;
    overflow: hidden;
    background: var(--backdrop);
    font-family: "Poppins", sans-serif;
  }
  .card {
    position: absolute;
    left: 264px;
    width: 580px;
    height: 357px;
    background: var(--card-navy);
    overflow: hidden;
  }
  .card--front { top: 226px; }
  .card--back { top: 620px; }

  .accent-panel {
    position: absolute;
    inset: 0;
    width: 100%;
    height: 100%;
  }

  .identity {
    position: absolute;
    left: 27px;
    top: 82px;
  }
  .identity__name {
    font-weight: 600;
    font-size: 22px;
    line-height: 1.1;
    letter-spacing: 0.2px;
    background: linear-gradient(90deg, var(--aqua), var(--azure));
    -webkit-background-clip: text;
    background-clip: text;
    color: transparent;
    text-transform: uppercase;
  }
  .identity__title {
    font-weight: 400;
    font-size: 17px;
    line-height: 1.2;
    color: var(--white);
  }

  .contact-list {
    position: absolute;
    left: 27px;
    top: 216px;
    list-style: none;
  }
  .contact-list__item {
    display: flex;
    align-items: center;
    gap: 7px;
    height: 21px;
    font-size: 17px;
    color: var(--white);
  }
  .contact-list__icon { width: 15px; height: 15px; flex: none; }

  .brand {
    position: absolute;
    inset: 0;
    display: flex;
    align-items: center;
    justify-content: center;
    gap: 16px;
  }
  .brand__dot {
    width: 48px;
    height: 48px;
    border-radius: 50%;
    background: var(--sky);
  }
  .brand__name {
    font-weight: 600;
    font-size: 46px;
    color: var(--white);
    letter-spacing: 0.5px;
  }
</style>
</head>
<body>
  <section class="card card--front">
    <svg class="accent-panel" viewBox="0 0 580 357" aria-hidden="true">
      <defs>
        <linearGradient id="accentFill" x1="0" y1="0" x2="1" y2="0">
          <stop offset="0" stop-color="#35e6ee"/>
          <stop offset="1" stop-color="#29a6ec"/>
        </linearGradient>
      </defs>
      <polygon points="350,0 580,0 580,357 290,357" fill="url(#accentFill)"/>
    </svg>

    <div class="identity">
      <h1 class="identity__name">Daniel Harlow</h1>
      <p class="identity__title">Managing Director</p>
    </div>

    <ul class="contact-list">
      <li class="contact-list__item">
        <svg class="contact-list__icon" viewBox="0 0 24 24" aria-hidden="true">
          <path d="M6.6 10.8a15 15 0 0 0 6.6 6.6l2.2-2.2c.3-.3.7-.4 1-.2 1.1.4 2.3.6 3.6.6.6 0 1 .4 1 1V20c0 .6-.4 1-1 1A17 17 0 0 1 3 4c0-.6.4-1 1-1h3.5c.6 0 1 .4 1 1 0 1.3.2 2.5.6 3.6.1.3 0 .7-.2 1z" fill="#2fb6ec"/>
        </svg>
        <span>044-987 650 312</span>
      </li>
      <li class="contact-list__item">
        <svg class="contact-list__icon" viewBox="0 0 24 24" aria-hidden="true">
          <rect x="1" y="5" width="22" height="14" fill="#2fb6ec"/>
          <path d="M1 5l11 8 11-8" fill="none" stroke="#22344e" stroke-width="1.6"/>
        </svg>
        <span>hello@verostelmail.com</span>
      </li>
      <li class="contact-list__item">
        <svg class="contact-list__icon" viewBox="0 0 24 24" aria-hidden="true">
          <g fill="none" stroke="#2fb6ec" stroke-width="1.8">
            <circle cx="12" cy="12" r="10"/>
            <ellipse cx="12" cy="12" rx="4.5" ry="10"/>
            <path d="M2 12h20M4 7h16M4 17h16"/>
          </g>
        </svg>
        <span>www.verostel-exchange.com</span>
      </li>
    </ul>
  </section>

  <section class="card card--back">
    <div class="brand">
      <span class="brand__dot"></span>
      <span class="brand__name">VEROSTEL</span>
    </div>
  </section>
</body>
</html>
```